Organic CBD topicals needs product labels for body butters, roll on oils and massage oil candles

We are looking for product labels that fit our growing brand, We are yogi's making organic CBD infused topicals that help people with pain relief and healing through plant based creams and oils, naturally, without side effects. We have body butter balms that come in 2oz tins, we have massage oil candles in 6oz, mandala design tins with a lid, we have infused essential oils in frosted glass bottles with healing gemstone roller balls, we also make lip balms in both 1/2 oz tins and lip balm sticks, as well as a 2oz twist up body butter balm. I would like the labels to have a yogi/chakra feel to them. The body butter balms come in different strengths, so it would be great if the strongest 600mg start at the base chakra, using the chakre color scale and go up from there. 300mg, 150mg then pure CBD, then up the chakra scale for the other products, 1:1, 3:1 and 30:1 for the roll on essential oils and massage oil candles.

You can see our products here: www.pinewillowremedies.org

Lumen Body Butter Balm label 2 1/2" round.
Matching 2" label for the bottom of the tin with ingredients & instructions.
Massage Oil Candle label 1 1/2 round
Bottom of Candle label 2" round for ingredients & instructions
Spiral Lumen Body Butter Label 4 1'2 wide x 2 1/2 tall Square
Twist up lip balm label can be 2 1/4 w x 1 1/2 tall
Lip Balm tin label 1" round

Target Market(s)

Everyone that has pain, injuries, headaches, skin conditions, etc... and wants to deal with them naturally, without big pharma and their terrible medicines that come with killer side effects.

Font styles to use
Serif
Sans Serif

Requirements
Must have
• A yogi look and feel, chakra colors, symbols and our logo featured prominently
Should not have
• a corporate look or feel

```html
<!DOCTYPE html>
<html lang="en">
<head>
<meta charset="utf-8">
<title>Lumen Organic Body Butter Salve – Lid Label</title>
<link rel="stylesheet" href="https://fonts.googleapis.com/css2?family=Cinzel:wght@400;700&family=Quicksand:wght@400;500&display=swap">
<style>
  :root {
    --canvas: #ffffff;
    --label-white: #fdfdfb;
    --pattern-grey: #ecece6;
    --swirl-sage: #dcdcbc;
    --swirl-sage-light: #e6e6cc;
    --border-olive: #a39d2e;
    --border-band: #e2dfae;
    --ink-dark: #2b2622;
    --ink-grey: #4a4744;
    --rule-red: #b4524a;
    --salve-green: #6cab45;
    --lavender: #8a63b6;
    --lemon-olive: #9caa2c;
    --badge-green: #3aa14a;
    --mark-ring: #7a3b2a;
    --serif: "Cinzel", serif;
    --sans: "Quicksand", sans-serif;
  }
  html, body {
    margin: 0;
    padding: 0;
    width: 1200px;
    height: 654px;
    overflow: hidden;
    background: var(--canvas);
  }
  .canvas {
    position: relative;
    width: 1200px;
    height: 654px;
  }
  .lid-label {
    position: absolute;
    display: block;
  }
  .lid-label--large { left: 108px; top: 98px; width: 436px; height: 436px; }
  .lid-label--small { left: 717px; top: 141px; width: 374px; height: 374px; }
  .label-face { fill: var(--label-white); stroke: #e4e4e0; stroke-width: 1; }
  .face-pattern { fill: url(#face-pattern-tone); }
  .key-band { fill: none; stroke: var(--border-band); stroke-width: 12; }
  .key-frame { fill: none; stroke: var(--border-olive); stroke-width: 1.6; }
  .swirl { fill: url(#swirl-tone); }
  .brand-dot { fill: none; stroke: var(--mark-ring); stroke-width: 3; }
  .brand-name { font-family: var(--serif); font-weight: 400; fill: var(--ink-dark); font-size: 27px; letter-spacing: .5px; }
  .brand-line { font-family: var(--serif); font-weight: 400; fill: var(--ink-dark); font-size: 12.5px; letter-spacing: .3px; }
  .product-mark { font-family: var(--serif); font-weight: 700; fill: var(--ink-dark); font-size: 31px; }
  .product-organic { font-family: var(--serif); font-weight: 700; fill: var(--ink-dark); font-size: 26px; }
  .product-type { font-family: var(--sans); font-weight: 400; fill: var(--ink-grey); font-size: 24px; }
  .rule-red { stroke: var(--rule-red); stroke-width: 1.2; }
  .salve { font-family: var(--serif); font-weight: 400; fill: var(--salve-green); font-size: 18px; }
  .scent-lavender { font-family: var(--sans); font-weight: 500; fill: var(--lavender); font-size: 19px; }
  .scent-lemon { font-family: var(--sans); font-weight: 500; fill: var(--lemon-olive); font-size: 19px; }
  .rule-white { stroke: #ffffff; stroke-width: 2.5; }
  .seal { fill: var(--badge-green); }
  .seal-inner { fill: none; stroke: #ffffff; stroke-width: 2; }
</style>
</head>
<body>
<main class="canvas">
  <svg width="0" height="0" style="position:absolute" aria-hidden="true">
    <defs>
      <radialGradient id="face-pattern-tone" cx="50%" cy="45%" r="55%">
        <stop offset="0%" stop-color="#ffffff"/>
        <stop offset="100%" stop-color="#ecece6"/>
      </radialGradient>
      <radialGradient id="swirl-tone" cx="60%" cy="70%" r="60%">
        <stop offset="0%" stop-color="#e6e6cc"/>
        <stop offset="100%" stop-color="#d8d8b6"/>
      </radialGradient>
      <symbol id="lid-label-art" viewBox="0 0 500 500">
        <circle class="label-face" cx="250" cy="250" r="248"/>
        <circle class="face-pattern" cx="250" cy="250" r="222" role="img" aria-label="Faint flower-of-life background pattern"/>
        <path class="swirl" transform="rotate(22 250 250)"
              d="M250,28 A222,222 0 0 1 250,472 A111,111 0 0 1 250,250 A111,111 0 0 0 250,28 Z"
              role="img" aria-label="Sage swirl with faint lotus pattern"/>
        <g role="img" aria-label="Greek key border ring">
          <circle class="key-band" cx="250" cy="250" r="231"/>
          <circle class="key-frame" cx="250" cy="250" r="238"/>
          <circle class="key-frame" cx="250" cy="250" r="224"/>
        </g>
        <circle class="brand-dot" cx="250" cy="122" r="42"/>
        <text class="brand-name" x="250" y="205" text-anchor="middle">PINE WILLOW</text>
        <text class="brand-line" x="250" y="223" text-anchor="middle">ORGANIC REMEDIES</text>
        <text class="product-mark" x="250" y="322" text-anchor="middle">LUMEN</text>
        <text class="product-organic" x="250" y="348" text-anchor="middle">ORGANIC</text>
        <text class="product-type" x="250" y="376" text-anchor="middle">BODY BUTTER</text>
        <line class="rule-red" x1="174" y1="386" x2="326" y2="386"/>
        <text class="salve" x="250" y="406" text-anchor="middle">||SALVE||</text>
        <text class="scent-lavender" x="250" y="438" text-anchor="middle">LAVENDER</text>
        <text class="scent-lemon" x="250" y="459" text-anchor="middle">&amp; LEMON</text>
        <line class="rule-white" x1="180" y1="470" x2="320" y2="470"/>
        <circle class="seal" cx="410" cy="305" r="36"/>
        <circle class="seal-inner" cx="410" cy="305" r="28"/>
      </symbol>
    </defs>
  </svg>

  <svg class="lid-label lid-label--large" viewBox="0 0 500 500" role="img" aria-label="Lumen Organic Body Butter Salve, Lavender and Lemon, Pine Willow Organic Remedies">
    <use href="#lid-label-art"/>
  </svg>
  <svg class="lid-label lid-label--small" viewBox="0 0 500 500" role="img" aria-label="Lumen Organic Body Butter Salve, Lavender and Lemon, Pine Willow Organic Remedies">
    <use href="#lid-label-art"/>
  </svg>
</main>
</body>
</html>
```